We specialize in pizza, pasta and salads and are now offering TAKE & BAKE and GRAB & GO ...

Looking for either a 8.5" x 11" or similar for a instore display. WILL BE ON A SWIVELING HOLDER to catch customers attention.

**THIS IS A DOUBLE SIDED PRINT**

ONE SIDE will consist of WHAT'S FOR DINNER TONIGHT? and the following:
* Take & Bake"
* "Baked Pasta"
* Freshly made in house
* Lasagna
$13.50
- please include attached closeup picture and logo

THE OTHER SIDE will consist of
mini charcutier board.
* snack size charcutier delight *
* Enjoy the flavors of gourmet snacking, all in one convenient box!

PRICE $8.99

Winning design will be commissioned to design labels for "grab and go" for take and bake pasta, charcuterie box, pasta salads, candy etc.

Thank you and please do not hesitate to ask any questions.

www.calderipizza.ca
www.fernloop.ca
Logo to be interchanged as they are affiliated meaning FernLoop is a brand within Calderi pizza.

Target Market(s)

our target market is customers who have already entered our business. This is to upsel

Industry/Entity Type

We are in a self serve enviroment and target business people

Requirements
Must have
• must be clean and catchy. We are located in a professional business community.
Nice to have
• Must be appealing, appetizing and utilize our website colors
Should not have
• should not have any carton drawings and not be cluttered (busy)

```html
<!DOCTYPE html>
<html lang="en">
<head>
<meta charset="utf-8">
<title>What's for Dinner Tonight? – Calderi Pizza</title>
<link rel="stylesheet" href="https://fonts.googleapis.com/css2?family=Federo&family=Open+Sans:wght@400;600&display=swap">
<style>
  :root {
    --paper: #f2f2f2;
    --ink: #4a4a4a;
    --rule: #5a5a5a;
    --accent: #c9302c;
    --frame: #c8594a;
    --price: #cc5a4a;
    --food-light: #eadfc4;
    --food-mid: #c08a3e;
    --food-dark: #6e4a20;
  }
  * { margin: 0; padding: 0; box-sizing: border-box; }
  html, body {
    width: 848px; height: 1200px; overflow: hidden;
    background: var(--paper);
  }
  .poster {
    position: relative; width: 848px; height: 1200px;
    background: var(--paper);
    font-family: "Federo", sans-serif;
    color: var(--ink);
  }
  .poster__art {
    position: absolute; inset: 0; width: 848px; height: 1200px;
  }
  .headline {
    position: absolute; left: 0; right: 0; top: 30px;
    text-align: center;
    font-size: 49px; line-height: 58px;
    letter-spacing: 0.5px;
    text-transform: uppercase;
    color: var(--ink);
  }
  .headline__accent { color: var(--accent); }
  .offer {
    position: absolute; left: 0; right: 0; top: 770px;
    list-style: none; text-align: center;
    font-size: 41px; line-height: 56.5px;
    text-transform: uppercase;
  }
  .offer__amp { color: var(--accent); }
  .price {
    position: absolute; left: 0; width: 848px; top: 1012px;
    padding-right: 12px;
    text-align: center;
    font-family: "Open Sans", sans-serif;
    font-weight: 400; font-size: 66px; line-height: 80px;
    color: var(--price);
  }
  .brand {
    position: absolute; left: 0; right: 0; top: 1126px;
    text-align: center;
    font-family: "Open Sans", sans-serif;
    font-weight: 400; font-size: 33px; line-height: 36px;
    letter-spacing: 0.5px;
    color: var(--ink);
  }
</style>
</head>
<body>
<main class="poster">
  <svg class="poster__art" viewBox="0 0 794 1123" xmlns="http://www.w3.org/2000/svg">
    <defs>
      <radialGradient id="food-tone" cx="0.5" cy="0.45" r="0.6">
        <stop offset="0" stop-color="var(--food-light)" style="stop-color:#eadfc4"/>
        <stop offset="0.55" stop-color="#c08a3e"/>
        <stop offset="1" stop-color="#6e4a20"/>
      </radialGradient>
    </defs>

    <!-- rules -->
    <line class="rule" x1="25" y1="18" x2="770" y2="18" stroke="#5a5a5a" stroke-width="2"/>
    <line class="rule" x1="25" y1="1100" x2="770" y2="1100" stroke="#5a5a5a" stroke-width="2"/>

    <!-- red frame -->
    <g class="frame" fill="none" stroke="#c8594a" stroke-width="3">
      <polyline points="42,60 25,60 25,1076 266,1076"/>
      <polyline points="752,60 770,60 770,1076 528,1076"/>
    </g>

    <!-- feature ring -->
    <circle class="feature-ring" cx="404" cy="420" r="282" fill="none" stroke="#5a5a5a" stroke-width="2"/>

    <g class="feature-photo" role="img" aria-label="Close-up of baked lasagna with stretching melted cheese, a slice lifted from the dish" fill="url(#food-tone)">
      <path d="M404,420 L184,288 A257,257 0 1 0 316,178 Z"/>
      <path d="M404,420 L184,288 A257,257 0 0 1 316,178 Z" transform="translate(-45,-68)"/>
    </g>
  </svg>

  <h1 class="headline">What's for <span class="headline__accent">Dinner</span> Tonight?</h1>

  <ul class="offer">
    <li>Take <span class="offer__amp">&amp;</span> Bake</li>
    <li>Baked Pasta</li>
    <li>Freshly Made</li>
    <li>In House Lasagna</li>
  </ul>

  <p class="price">$13.50</p>

  <p class="brand">CALDERI PIZZA</p>
</main>
</body>
</html>
```